Trondel Group letterhead

Hi,

I need a letterhead template created for our business. This should be done in word format and A4 size. The images need to not move in the template ie when I am adding writing in etc. and should flow on when I get to a second page.

I have attached our logo templates below.

Other details to include on the letterhead somewhere are:

0438 571 962
Max@Trondelelectrical.example.com.au
PO Box 781 Marrowdale NSW 2163
ABN: 57 318 492 076

Thanks!

```html
<!DOCTYPE html>
<html lang="en">
<head>
<meta charset="utf-8">
<title>Trondel Group Letterhead</title>
<link rel="stylesheet" href="https://fonts.googleapis.com/css2?family=Open+Sans:wght@400;600;700&display=swap">
<style>
  :root {
    --backdrop: #e6e7ea;
    --paper: #ffffff;
    --ink: #4a4b52;
    --ink-dark: #2b2c33;
    --accent: #e4572e;
    --charcoal: #3a3c45;
    --signature-fill: #f1f1f3;
  }
  * { box-sizing: border-box; margin: 0; padding: 0; }
  html, body {
    width: 1200px;
    height: 980px;
    overflow: hidden;
    background: var(--backdrop);
    font-family: "Open Sans", sans-serif;
    color: var(--ink);
  }
  .letterhead {
    position: absolute;
    left: 267px;
    top: 20px;
    width: 665px;
    height: 940px;
    background: var(--paper);
    box-shadow: 0 4px 18px rgba(0,0,0,0.12);
    overflow: hidden;
  }
  .brand {
    position: absolute;
    left: 60px;
    top: 96px;
    display: flex;
    align-items: center;
    gap: 10px;
  }
  .brand-dot {
    width: 30px;
    height: 30px;
    border-radius: 50%;
    background: var(--ink-dark);
  }
  .brand-name {
    font-size: 24px;
    font-weight: 700;
    color: var(--ink-dark);
    letter-spacing: 0.5px;
  }
  .contact {
    position: absolute;
    right: 60px;
    top: 52px;
    width: 250px;
    font-size: 12px;
    line-height: 1.45;
    color: var(--ink);
    list-style: none;
  }
  .contact li { display: flex; align-items: center; gap: 5px; white-space: nowrap; }
  .contact svg { width: 11px; height: 11px; flex: none; }
  .contact .icon-phone { fill: var(--accent); }
  .contact .icon-mail rect { fill: var(--accent); }
  .contact .icon-mail path { fill: none; stroke: var(--paper); stroke-width: 2; }
  .letter-body {
    position: absolute;
    left: 60px;
    top: 220px;
    width: 545px;
    font-size: 12.5px;
    line-height: 1.6;
  }
  .salutation { margin-bottom: 14px; }
  .letter-body p { margin-bottom: 16px; }
  .closing { margin-top: 6px; }
  .signature {
    display: block;
    width: 120px;
    height: 56px;
    margin-top: 16px;
    background: var(--signature-fill);
  }
  .footer-band {
    position: absolute;
    left: 0;
    bottom: 0;
    width: 100%;
    height: 14px;
    display: flex;
  }
  .footer-band .band-accent { flex: 0 0 80%; background: var(--accent); }
  .footer-band .band-dark { flex: 1; background: var(--charcoal); }
</style>
</head>
<body>
  <main class="letterhead">
    <header>
      <div class="brand">
        <span class="brand-dot"></span>
        <span class="brand-name">Trondel Group</span>
      </div>
      <ul class="contact">
        <li>PO Box 781 Marrowdale</li>
        <li>NSW 2163</li>
        <li>ABN: 57 318 492 076</li>
        <li>
          <svg class="icon-phone" viewBox="0 0 24 24" aria-hidden="true"><path d="M6.6 10.8a15.1 15.1 0 0 0 6.6 6.6l2.2-2.2a1 1 0 0 1 1-.25 11.4 11.4 0 0 0 3.6.57 1 1 0 0 1 1 1V20a1 1 0 0 1-1 1A17 17 0 0 1 3 4a1 1 0 0 1 1-1h3.5a1 1 0 0 1 1 1c0 1.25.2 2.45.57 3.57a1 1 0 0 1-.25 1z"/></svg>
          0438 571 962
        </li>
        <li>
          <svg class="icon-mail" viewBox="0 0 24 24" aria-hidden="true"><rect x="2" y="5" width="20" height="14" rx="1"/><path d="M3 6l9 7 9-7"/></svg>
          Max@Trondelelectrical.example.com.au
        </li>
      </ul>
    </header>

    <section class="letter-body">
      <p class="salutation">Dear customer,</p>
      <p>Lorem ipsum dolor sit amet, consectetur adipisicing elit, sed do eiusmod tempor incididunt ut labore et dolore magna aliqua. Ut enim ad minim veniam, quis nostrud exercitation ullamco laboris nisi ut aliquip ex ea commodo consequat. Duis aute irure dolor in reprehenderit in voluptate velit esse cillum dolore eu fugiat nulla pariatur. Excepteur sint occaecat cupidatat non proident, sunt in culpa qui officia deserunt mollit anim id est laborum.</p>
      <p>Lorem ipsum dolor sit amet, consectetur adipisicing elit, sed do eiusmod tempor incididunt ut labore et dolore magna aliqua. Ut enim ad minim veniam, quis nostrud exercitation ullamco laboris nisi ut aliquip ex ea commodo consequat. Duis aute irure dolor in reprehenderit in voluptate velit esse cillum dolore eu fugiat nulla pariatur. Excepteur sint occaecat cupidatat non proident, sunt in culpa qui officia deserunt mollit anim id est laborum.</p>
      <p>Lorem ipsum dolor sit amet, consectetur adipisicing elit, sed do eiusmod tempor incididunt ut labore et dolore magna aliqua. Ut enim ad minim veniam, quis nostrud exercitation ullamco laboris nisi ut aliquip ex ea commodo consequat. Duis aute irure dolor in reprehenderit in voluptate velit esse cillum dolore eu fugiat nulla pariatur. Excepteur sint occaecat cupidatat non proident, sunt in culpa qui officia deserunt mollit anim id est laborum.</p>
      <p>Lorem ipsum dolor sit amet, consectetur adipisicing elit, sed do eiusmod tempor incididunt ut labore et dolore magna aliqua. Ut enim ad minim veniam, quis nostrud exercitation ullamco laboris nisi ut aliquip ex ea commodo consequat. Duis aute irure dolor in reprehenderit.</p>
      <p class="closing">Yours Sincerely,</p>
      <span class="signature" role="img" aria-label="Handwritten signature of the sender"></span>
    </section>

    <footer class="footer-band">
      <span class="band-accent"></span>
      <span class="band-dark"></span>
    </footer>
  </main>
</body>
</html>
```